KT Crewing business card

Require business card which includes:
Company name: KT CREWING PTY LTD
Email: Mick@ktcrewing.com.au
Phone: 0431 256 049
ACN: 718 235 946

slogan: Onsite Auto Electrician Labour hire

Details and logo on top side
Logo only on bottom side

colour codes : #F15A29 , #939598

Target Market(s)

Western Australia mining sector

Industry/Entity Type

Mining

Contact Information for Business Card

Require business card which includes: Company name: KT CREWING PTY LTD Email: Mick@ktcrewing.com.au Phone: 0431 256 049 ACN: 718 235 946 slogan: Onsite Auto Electrician Labour hire Details and logo on top side Logo only on bottom side colour codes : #F15A29 , #939598

Colors
EE7325
F08F49
F5BC92
FAE3D3
FDF4ED

Requirements
Must have
• double sided

```html
<!DOCTYPE html>
<html lang="en">
<head>
<meta charset="utf-8">
<title>KT Crewing – Business Card</title>
<link rel="stylesheet" href="https://fonts.googleapis.com/css2?family=Quicksand:wght@500;700&display=swap">
<style>
  :root {
    --brand-orange: #F15A29;
    --brand-grey: #939598;
    --grey-dark: #7d7f82;
    --grey-light: #b3b5b8;
    --paper: #ffffff;
    --backdrop: #e9e7e4;
  }
  * { margin: 0; padding: 0; box-sizing: border-box; }
  html, body {
    width: 1200px; height: 913px; overflow: hidden;
    background: var(--backdrop);
    font-family: "Quicksand", sans-serif;
  }
  .canvas { position: relative; width: 1200px; height: 913px; }
  .card {
    position: absolute;
    width: 540px; height: 309px;
    background: var(--brand-orange);
    box-shadow: 0 6px 18px rgba(0,0,0,0.18);
    overflow: hidden;
  }
  .card-front { left: 40px; top: 302px; }
  .card-back  { left: 620px; top: 302px; }
  .card-shape { position: absolute; inset: 0; width: 100%; height: 100%; }

  .wordmark {
    position: absolute;
    color: var(--brand-orange);
    font-weight: 700;
    white-space: nowrap;
    letter-spacing: 0.5px;
  }
  .card-front .wordmark { left: 28px; top: 124px; font-size: 34px; }
  .card-back .wordmark  { right: 28px; top: 62px; font-size: 44px; }

  .company-block {
    position: absolute; right: 22px; bottom: 26px;
    width: 240px; text-align: right; color: var(--paper);
  }
  .company-name { font-size: 14px; font-weight: 500; padding-bottom: 6px; }
  .rule { height: 1px; background: var(--paper); margin-bottom: 7px; }
  .slogan { font-size: 13px; font-weight: 500; white-space: nowrap; }

  .acn {
    position: absolute; left: 24px; top: 22px;
    color: #5d5f62; font-size: 15px; font-weight: 500;
  }
  .acn .acn-number { color: var(--paper); }

  .contact-block {
    position: absolute; left: 24px; bottom: 28px; width: 360px;
    color: var(--paper);
  }
  .contact-line { font-size: 15px; font-weight: 500; line-height: 1.45; }
  .contact-block .rule { margin: 8px 0 8px; }
  .contact-block .slogan { font-size: 17px; font-weight: 700; }
</style>
</head>
<body>
<main class="canvas">

  <section class="card card-front" aria-label="Business card front">
    <svg class="card-shape" viewBox="0 0 540 309" preserveAspectRatio="none" aria-hidden="true">
      <path d="M0,0 L208,0 Q352,64 282,309 L0,309 Z" fill="var(--grey-dark)"/>
      <path d="M0,0 L192,0 Q342,62 268,309 L0,309 Z" fill="var(--grey-light)"/>
      <path d="M0,0 L170,0 Q330,60 250,309 L0,309 Z" fill="var(--paper)"/>
    </svg>
    <div class="wordmark">KT Crewing</div>
    <div class="company-block">
      <p class="company-name">KT CREWING PTY LTD</p>
      <div class="rule"></div>
      <p class="slogan">Onsite Auto Electrician Labour hire</p>
    </div>
  </section>

  <section class="card card-back" aria-label="Business card back">
    <svg class="card-shape" viewBox="0 0 540 309" preserveAspectRatio="none" aria-hidden="true">
      <path d="M228,0 Q250,262 540,300 L540,0 Z" fill="var(--grey-dark)"/>
      <path d="M240,0 Q266,252 540,290 L540,0 Z" fill="var(--grey-light)"/>
      <path d="M256,0 Q284,240 540,278 L540,0 Z" fill="var(--paper)"/>
    </svg>
    <div class="wordmark">KT Crewing</div>
    <p class="acn">ACN: <span class="acn-number">718 235 946</span></p>
    <div class="contact-block">
      <p class="contact-line">P. 0431 256 049</p>
      <p class="contact-line">E. Mick@ktcrewing.com.au</p>
      <div class="rule"></div>
      <p class="slogan">Onsite Auto Electrician Labour hire</p>
    </div>
  </section>

</main>
</body>
</html>
```